terras letterhead

We would like to create a new letterhead that our company will use for proposals, invoices, statements and letters. Our company name is Terra-Vantage. We are a landscape design/build and landscape maintenance company. We have a web site Terra-Vantage.example where our logo (the leaf with the lettering within it only) is displayed.

Industry/Entity Type

Graphic Design

Requirements
Must have
• Address and info on our current letterhead (uploaded)
Nice to have
• We would like the design to look presentable in grey scale as well as color.
Should not have
• Do not want to infringe much on the normal useable area within the normal print areas.

```html
<!DOCTYPE html>
<html lang="en">
<head>
<meta charset="utf-8">
<title>Terra-Vantage Letterhead</title>
<link href="https://fonts.googleapis.com/css2?family=Caladea:wght@400;700&display=swap" rel="stylesheet">
<style>
  :root {
    --ink: #2b2b2b;
    --brand-green: #1f4d2b;
    --accent-green: #8dc63f;
    --link-blue: #3b5bbf;
    --wash-light: #ffffff;
    --wash-green: #cfe2cc;
    --paper: #ffffff;
  }
  html, body {
    margin: 0;
    padding: 0;
    overflow: hidden;
    background: var(--paper);
  }
  .letterhead {
    position: relative;
    width: 927px;
    height: 1200px;
    overflow: hidden;
    background: var(--paper);
    font-family: "Caladea", Georgia, serif;
    color: var(--ink);
  }
  .corner-wash {
    position: absolute;
    top: 0;
    left: 0;
    width: 927px;
    height: 260px;
  }
  .brand {
    position: absolute;
    left: 40px;
    top: 72px;
    display: flex;
    align-items: center;
    gap: 14px;
  }
  .brand-dot {
    width: 22px;
    height: 22px;
    border-radius: 50%;
    background: var(--brand-green);
  }
  .brand-name {
    font-size: 38px;
    font-weight: 700;
    color: var(--brand-green);
    letter-spacing: 0.5px;
  }
  .contact {
    position: absolute;
    right: 62px;
    top: 46px;
    text-align: right;
    font-size: 17px;
    line-height: 22px;
  }
  .contact p { margin: 0; }
  .contact .online { margin-top: 22px; }
  .contact a {
    color: var(--link-blue);
    text-decoration: underline;
  }
  .footer-rule {
    position: absolute;
    left: 0;
    top: 1093px;
    width: 927px;
    height: 3px;
    background: var(--accent-green);
  }
  .footer-address {
    position: absolute;
    left: 0;
    top: 1126px;
    width: 927px;
    text-align: center;
    font-size: 13px;
    line-height: 19px;
  }
  .footer-address p { margin: 0; }
</style>
</head>
<body>
  <div class="letterhead">
    <svg class="corner-wash" viewBox="0 0 927 260" aria-hidden="true">
      <defs>
        <linearGradient id="washGradient" x1="0" y1="0" x2="1" y2="0.3">
          <stop offset="0" stop-color="var(--wash-light)"/>
          <stop offset="1" stop-color="var(--wash-green)"/>
        </linearGradient>
      </defs>
      <path d="M424 0 C 470 140, 680 250, 927 232 L927 0 Z" fill="url(#washGradient)"/>
    </svg>

    <div class="brand">
      <span class="brand-dot"></span>
      <span class="brand-name">Terra-Vantage</span>
    </div>

    <div class="contact">
      <p>Tel: 908.555.0142</p>
      <p>Fax: 908.555.0187</p>
      <p class="online"><a href="mailto:service@terra-vantage.example">service@terra-vantage.example</a></p>
      <p>www.terra-vantage.example</p>
    </div>

    <div class="footer-rule"></div>
    <div class="footer-address">
      <p>118 Meadowbrook Lane, Westfield Hollow, NJ 07090</p>
      <p>Terra-Vantage</p>
    </div>
  </div>
</body>
</html>
```